Flyer-Design für betriebliche Gesundheitsvorsorge
Zielgruppe
'Werk im Schwung' soll Unternehmen die Möglichkeit bieten unsere Dienste im Sinne der Gesundheitsvorsorge für ihre Mitarbeiter in Anspruch zu nehmen. Dies beinhaltet Massagen am Arbeitsplatz (in separaten Räumlichkeiten), Arbeitsplatzberatung bezgl. Ergonomie, Workshops zu kurzen Übungen die in den Arbeitsalltag integriert werden können, Verdeutlichung der Eigenverantwortung für einen gesunden Körper, ....
Aufgabenstellung
Die Werbekarte sollte in DIN Lang format sein.

```html
<!DOCTYPE html>
<html lang="de">
<head>
<meta charset="utf-8">
<title>Werk im Schwung – Werbekarte DIN Lang</title>
<link rel="stylesheet" href="https://fonts.googleapis.com/css2?family=Montserrat:wght@300;400;500;600;700;800&display=swap">
<style>
  :root {
    --teal: #7ebfb5;
    --grey-text: #555a5e;
    --grey-dark: #3f4448;
    --paper: #ffffff;
    --backdrop: #d6d8da;
  }
  * { box-sizing: border-box; margin: 0; padding: 0; }
  html, body {
    width: 1200px; height: 1200px; overflow: hidden;
    background: var(--backdrop);
    font-family: "Montserrat", Arial, sans-serif;
    color: var(--grey-text);
  }
  .card {
    position: absolute; left: 100px;
    width: 1000px; height: 472px;
    background: var(--paper);
    overflow: hidden;
    box-shadow: 0 6px 18px rgba(0,0,0,0.18);
  }
  .card--front { top: 84px; }
  .card--back { top: 644px; }

  .brand { position: absolute; left: 40px; top: 36px; z-index: 3; }
  .brand__row { display: flex; align-items: center; gap: 14px; }
  .brand__dot { width: 44px; height: 44px; border-radius: 50%; background: var(--teal); }
  .brand__name { font-size: 32px; font-weight: 600; color: var(--teal); }
  .brand__tagline { margin-top: 4px; margin-left: 58px; font-size: 14px; font-weight: 500; color: var(--grey-text); letter-spacing: 0.5px; }

  .website { position: absolute; right: 40px; top: 36px; font-size: 19px; font-weight: 600; color: var(--grey-dark); }

  .services { position: absolute; left: 40px; top: 160px; width: 540px; font-size: 17px; line-height: 1.55; color: var(--grey-text); }
  .services .sep { color: var(--teal); font-weight: 600; }

  .photo { position: absolute; }
  .photo--neck { left: 40px; top: 270px; width: 170px; height: 130px; background: linear-gradient(135deg, #a9b4bd, #6e7a86); }
  .photo--worker { left: 214px; top: 270px; width: 170px; height: 130px; background: linear-gradient(135deg, #c9c2b6, #8c8f95); }
  .photo--office { left: 388px; top: 270px; width: 170px; height: 130px; background: linear-gradient(135deg, #dfe4ea, #9fb0c4); }
  .photo--car { left: 610px; top: 80px; width: 350px; height: 200px; background: linear-gradient(160deg, #f4f4f4, #d9dcdf); border-radius: 6px; }
  .photo--bench { left: 575px; top: 260px; width: 140px; height: 112px; background: linear-gradient(135deg, #3a3a3a, #161616); border-radius: 6px; }

  .contact { position: absolute; right: 40px; top: 316px; text-align: right; font-size: 15px; line-height: 1.6; color: var(--grey-dark); }

  .band { position: absolute; left: 0; bottom: 0; width: 100%; height: 72px; background: var(--teal); display: flex; align-items: center; z-index: 2; }
  .band__claim { padding-left: 40px; color: #fff; font-size: 25px; font-weight: 700; white-space: nowrap; }
  .band--back { justify-content: flex-end; }
  .band__motto { padding-right: 40px; color: #fff; font-size: 24px; font-weight: 300; white-space: nowrap; }
  .band__motto strong { font-weight: 800; }

  .photo--massage { left: 0; top: 128px; width: 520px; height: 344px; background: linear-gradient(135deg, #e8e9ec, #a8b2bf); z-index: 1; }

  .benefits { position: absolute; left: 570px; top: 40px; width: 400px; }
  .benefits__title { font-size: 21px; font-weight: 700; color: var(--teal); line-height: 1.3; }
  .benefits__list { list-style: none; margin-top: 16px; }
  .benefits__item { display: flex; gap: 10px; font-size: 15px; line-height: 1.4; color: var(--grey-dark); margin-bottom: 8px; }
  .benefits__item svg { flex: 0 0 16px; margin-top: 3px; }
</style>
</head>
<body>

<section class="card card--front">
  <div class="brand">
    <div class="brand__row"><span class="brand__dot"></span><span class="brand__name">Werk im Schwung</span></div>
    <p class="brand__tagline">Gesundheitsvorsorge am Arbeitsplatz</p>
  </div>
  <p class="website">www.werkimschwung.com</p>

  <p class="services">
    Präventive Intervention bei haltungsbedingten Schmerzen<br>
    Heilmassage <span class="sep">//</span> Sportmassage <span class="sep">//</span> Bindegewebsmassage<br>
    Schröpfen <span class="sep">//</span> Aromatherapie <span class="sep">//</span> Kinesio Taping
  </p>

  <div class="photo photo--neck" role="img" aria-label="Foto: Mann im Büro mit Nackenschmerzen"></div>
  <div class="photo photo--worker" role="img" aria-label="Foto: Bauarbeiter mit Rückenschmerzen vor einem Gebäude"></div>
  <div class="photo photo--office" role="img" aria-label="Foto: Person am Schreibtisch mit Rückenschmerzen"></div>
  <div class="photo photo--car" role="img" aria-label="Foto: Therapeutin neben weißem Firmenauto"></div>
  <div class="photo photo--bench" role="img" aria-label="Foto: zusammengeklappte mobile Massageliege"></div>

  <p class="contact">+43 (0) 660 482 3917<br>hallo@werkimschwung.com</p>

  <div class="band"><p class="band__claim">Werk im Schwung – Gesundheitsvorsorge an Ihrem Arbeitsplatz</p></div>
</section>

<section class="card card--back">
  <div class="brand">
    <div class="brand__row"><span class="brand__dot"></span><span class="brand__name">Werk im Schwung</span></div>
    <p class="brand__tagline">Gesundheitsvorsorge am Arbeitsplatz</p>
  </div>

  <div class="photo photo--massage" role="img" aria-label="Foto: Mann erhält Rückenmassage auf einem Massagestuhl"></div>

  <div class="benefits">
    <h2 class="benefits__title">Lassen Sie sich von Gesundheit am Arbeitsplatz überzeugen!</h2>
    <ul class="benefits__list">
      <li class="benefits__item"><svg width="16" height="14" viewBox="0 0 16 14"><path d="M1 7.5 L6 12 L15 1.5" fill="none" stroke="#7ebfb5" stroke-width="2.6" stroke-linecap="round" stroke-linejoin="round"/></svg><span>Direkt an Ihrem Arbeitsplatz</span></li>
      <li class="benefits__item"><svg width="16" height="14" viewBox="0 0 16 14"><path d="M1 7.5 L6 12 L15 1.5" fill="none" stroke="#7ebfb5" stroke-width="2.6" stroke-linecap="round" stroke-linejoin="round"/></svg><span>Keine weiten Umwege für Sie</span></li>
      <li class="benefits__item"><svg width="16" height="14" viewBox="0 0 16 14"><path d="M1 7.5 L6 12 L15 1.5" fill="none" stroke="#7ebfb5" stroke-width="2.6" stroke-linecap="round" stroke-linejoin="round"/></svg><span>Während Ihrer Arbeitszeit können Sie sich angenehm behandeln lassen</span></li>
      <li class="benefits__item"><svg width="16" height="14" viewBox="0 0 16 14"><path d="M1 7.5 L6 12 L15 1.5" fill="none" stroke="#7ebfb5" stroke-width="2.6" stroke-linecap="round" stroke-linejoin="round"/></svg><span>Behandlungen werden individuell an Ihre Bedürfnisse angepasst</span></li>
      <li class="benefits__item"><svg width="16" height="14" viewBox="0 0 16 14"><path d="M1 7.5 L6 12 L15 1.5" fill="none" stroke="#7ebfb5" stroke-width="2.6" stroke-linecap="round" stroke-linejoin="round"/></svg><span>Unser Team bildet sich ständig weiter, um den besten Service in jeder Situation für Sie zu erreichen</span></li>
    </ul>
  </div>

  <div class="band band--back">
    <p class="band__motto"><strong>HEALTHY</strong> BODY // <strong>HEALTHY</strong> MIND // <strong>HEALTHY</strong> SOUL</p>
  </div>
</section>

</body>
</html>
```